Professional, elegant brochure for funeral home

We have a funeral home. We would like a 2 sided brochure. On one side will be 3 columns for our cremation options and on the other side would be 2-3 columns of our burial options. Would like to print it and also will be putting it on our website at www.Veltranoserves.com

Use as examples

https://www.bardwellhaven.com/pricing-and-resources/online-cremation-package-options

https://pellingtonmortuary.com/wp-content/uploads/Cremation-with-Ceremony-Plans.pdf

We only need a simple 1page (front and back brochure). Once we have decided on the designer I can provide the final content to be placed on the brochure.

Target Market(s)

We are family owned business so Something soft, inviting, personable and looks professionally done.

Industry/Entity Type

Funeral Home

Requirements
Must have
• Look professional. Easy to read
Nice to have
• Softer Muted comforting colors. No bright colors.

```html
<!DOCTYPE html>
<html lang="en">
<head>
<meta charset="utf-8">
<title>Veltrano Funeral Home – Cremation &amp; Burial Brochure</title>
<link rel="stylesheet" href="https://fonts.googleapis.com/css2?family=Cinzel:wght@400;700&family=Lato:ital,wght@0,400;0,700;0,900;1,400;1,700;1,900&display=swap">
<style>
  :root{
    --bg:#8f8f8f;
    --paper:#ffffff;
    --ink:#2b2b2b;
    --muted:#444;
    --green:#9cbf2f;
    --green-light:#d6e86e;
    --blue:#1b6db0;
    --blue-dark:#0f5a99;
    --grey-card:#e6e6e6;
    --title-grey:#4a4a4a;
  }
  *{margin:0;padding:0;box-sizing:border-box}
  html,body{width:1200px;height:900px;overflow:hidden}
  body{background:linear-gradient(180deg,#9a9a9a,#6f6f6f);font-family:'Lato',sans-serif;color:var(--ink);position:relative}
  .page{position:absolute;top:92px;height:708px;background:var(--paper);overflow:hidden;box-shadow:0 2px 8px rgba(0,0,0,.25)}
  .page--cremation{left:82px;width:501px}
  .page--burial{left:637px;width:503px}
  .abs{position:absolute;z-index:2}
  .photo{position:absolute;z-index:0}

  /* Cremation side */
  .photo--blossoms{left:0;top:0;width:250px;height:310px;background:radial-gradient(ellipse at 30% 35%,#f4f1e6 0%,#c9d79b 40%,#eef2e0 70%,rgba(255,255,255,0) 100%)}
  .title{font-family:'Cinzel',serif;text-align:center;line-height:1}
  .title--storied{left:230px;width:250px;top:38px;font-size:40px;color:var(--title-grey)}
  .title--ever{left:230px;width:250px;top:72px;font-size:66px;color:var(--green)}
  .title--after{left:220px;width:270px;top:128px;font-size:68px;color:var(--blue)}
  .tagline{left:102px;width:380px;top:210px;font-size:13.5px;font-weight:900;font-style:italic}
  .intro{left:100px;width:375px;top:233px;font-size:7.4px;line-height:1.4;font-style:italic;font-weight:700;color:var(--muted)}
  .band{position:absolute;z-index:2;color:#fff;font-weight:700;display:flex;align-items:center}
  .band--cremation{left:0;top:305px;width:501px;height:33px;justify-content:center;font-size:17px;letter-spacing:.3px;
    background:linear-gradient(90deg,rgba(27,109,176,.25) 0%,var(--blue) 22%,var(--blue) 78%,rgba(27,109,176,.25) 100%)}
  .lead{left:26px;width:450px;top:344px;font-size:7.4px;line-height:1.4;font-style:italic;font-weight:700;color:var(--muted)}
  .option{position:absolute;z-index:2;top:440px;height:158px;border-radius:4px;padding:38px 8px 0}
  .option--green{background:var(--green-light)}
  .option--grey{background:var(--grey-card)}
  .option__tab{position:absolute;top:-24px;left:11px;right:8px;height:48px;color:#fff;font-size:11.5px;font-weight:700;font-style:italic;display:flex;align-items:center;justify-content:center;text-align:center;line-height:1.2}
  .option__tab--blue{background:var(--blue-dark)}
  .option__tab--green{background:var(--green)}
  .option__rule{position:absolute;top:30px;left:20px;right:20px;height:1px;background:var(--blue)}
  .option__rule::after{content:"";position:absolute;left:50%;top:-2px;width:5px;height:5px;border-radius:50%;background:var(--blue);transform:translateX(-50%)}
  .option__text{font-size:7.2px;line-height:1.38;font-style:italic;font-weight:700;color:var(--muted)}
  .option--one{left:14px;width:150px;text-align:justify}
  .option--two{left:176px;width:150px}
  .option--three{left:333px;width:154px}
  .photo--bouquet{left:328px;top:600px;width:173px;height:108px;background:radial-gradient(ellipse at 45% 55%,#e46aa0 0%,#f1b0c8 30%,#cfe1b5 58%,rgba(255,255,255,0) 80%)}
  .brand{display:flex;align-items:center;gap:6px;font-family:'Lato',sans-serif;font-weight:700;color:var(--blue);font-size:13px;line-height:1.15}
  .brand__dot{width:12px;height:12px;border-radius:50%;background:var(--green);flex:none}
  .brand--left{left:22px;top:630px;width:140px}
  .divider{left:168px;top:628px;width:1px;height:46px;background:#bbb}
  .contact{left:180px;top:630px;text-align:center}
  .contact__phone{font-size:18px;font-style:italic;font-weight:700;color:var(--blue)}
  .contact__web{font-size:9.5px;letter-spacing:1.5px;color:var(--muted);margin-top:2px}

  /* Burial side */
  .photo--rose{left:0;top:0;width:300px;height:708px;background:linear-gradient(90deg,#8d8a8a 0%,#c9b7b8 35%,#e9e4e4 65%,rgba(255,255,255,0) 100%)}
  .title--about{left:180px;width:290px;top:54px;font-size:42px;color:var(--green)}
  .title--burials{left:170px;width:310px;top:96px;font-size:60px;color:var(--blue-dark)}
  .subtitle{left:211px;width:265px;top:150px;font-size:14px;font-weight:900;font-style:italic;line-height:1.3}
  .body{font-size:7.4px;line-height:1.35;color:var(--muted)}
  .body--intro{left:211px;width:265px;top:191px;text-align:justify}
  .band--section{height:22px;justify-content:center;font-size:12.5px;padding-left:40px}
  .band--graveside{left:240px;top:262px;width:263px;background:linear-gradient(90deg,rgba(156,191,47,0) 0%,var(--green) 30%)}
  .band--committal{left:248px;top:427px;width:255px;background:linear-gradient(90deg,rgba(27,109,176,0) 0%,var(--blue-dark) 30%)}
  .band--immediate{left:243px;top:516px;width:260px;background:linear-gradient(90deg,rgba(156,191,47,0) 0%,var(--green) 30%)}
  .kicker{font-size:9.5px;font-weight:900;font-style:italic;color:var(--ink)}
  .kicker--graveside{left:220px;width:253px;top:292px;text-align:center;line-height:1.3}
  .body--graveside{left:217px;width:262px;top:318px;font-size:7px;line-height:1.25}
  .kicker--committal{left:60px;width:415px;top:461px;text-align:right}
  .body--committal{left:25px;width:452px;top:477px}
  .kicker--immediate{left:60px;width:415px;top:550px;text-align:right}
  .body--immediate{left:23px;width:452px;top:566px}
  .photo--roses{left:270px;top:600px;width:233px;height:108px;background:linear-gradient(180deg,rgba(255,255,255,0) 0%,#d8c99a 35%,#7a3a25 70%,#5a2a1b 100%)}
  .brand--right{left:34px;top:640px;width:140px;font-size:14px}
</style>
</head>
<body>

<section class="page page--cremation" aria-label="Cremation services side">
  <div class="photo photo--blossoms" role="img" aria-label="White blossoms on a flowering branch"></div>
  <h1 class="abs title title--storied">Storied</h1>
  <div class="abs title title--ever">EVER</div>
  <div class="abs title title--after">AFTER</div>
  <p class="abs tagline">Honor and celebrate life in a setting fit for remembering legends</p>
  <p class="abs intro">The Arthur J. Veltrano Funeral Home is a family business serving the Maple Ridge, NY area that is steeped in tradition. Its rich heritage reflects the value and vision of a respected family, well known for its commitment to excellence. Its founder, Arthur J. Veltrano, graduated first in his class from the Hollis School of Mortuary Science in Syracuse, in 1959. Classmates, professors and the general public all took early note of the tireless dedication and passion young Arthur possessed in providing families with outstanding funeral service.</p>

  <h2 class="band band--cremation">ALL ABOUT CREMATION SERVICES</h2>
  <p class="abs lead">Many people are choosing to cremate, but that doesn't mean they have to sacrifice the healing elements of a traditional burial. Let us help you create a memorial onsite—because it's helpful for many families to have a physical marker of remains. We can provide a range of flowers and décor accessories so you can honor your loved one. An onsite memorial becomes a place to commemorate a life and gather beyond the home, at a permanent and meaningful location. In addition, please know you can bring remains to the cemetery any time, even long after cremation. For more information about our cremation services in Maple Ridge, NY, please contact us today.</p>

  <article class="option option--green option--one">
    <h3 class="option__tab option__tab--blue">Funeral Service with Cremation as Final Disposition</h3>
    <span class="option__rule"></span>
    <p class="option__text">Similar to a traditional funeral service, the body of the deceased is placed in a cremation or rental casket for the funeral service. Cremation is performed after the service and the cremated remains are returned to the family. If you would like more information about our cremation services and options, please contact us today.</p>
  </article>
  <article class="option option--grey option--two">
    <h3 class="option__tab option__tab--green">Committal Service with Cremation as Final Disposition</h3>
    <span class="option__rule"></span>
    <p class="option__text">This act can be an important way to begin to let go. And it can be a creative, thoughtful reflection of your loved one. From sending remains in to space to letting them go at sea, we can help you plan a unique way to memorialize a life through scattering cremated remains.</p>
  </article>
  <article class="option option--green option--three">
    <h3 class="option__tab option__tab--blue">Ash Scattering</h3>
    <span class="option__rule"></span>
    <p class="option__text">A beautiful service that is held at the cemetery, following a funeral at mortuary chapel or your place of religious worship. Gather around your loved one's cremated remains to commemorate their life and honor the memories shared. This symbolic service is a beautiful step forward in the healing process, and can accompany many end of life options.</p>
  </article>

  <div class="photo photo--bouquet" role="img" aria-label="Hand laying a bouquet of pink and white flowers"></div>
  <div class="abs brand brand--left"><span class="brand__dot"></span><span>Arthur J. Veltrano<br>Funeral Home</span></div>
  <span class="abs divider"></span>
  <div class="abs contact">
    <div class="contact__phone">(716) 555-0142</div>
    <div class="contact__web">www.veltranofh.com</div>
  </div>
</section>

<section class="page page--burial" aria-label="Burial services side">
  <div class="photo photo--rose" role="img" aria-label="Mourner holding a single red rose, softly faded"></div>
  <h1 class="abs title title--about">All About</h1>
  <div class="abs title title--burials">Burials</div>
  <p class="abs subtitle">Traditional. Profound. Healing. Design a permanent resting place for your loved one</p>
  <p class="abs body body--intro">Burials are a traditional memorial choice that give families a meaningful physical symbol to mark a loved one's resting place. At Arthur J. Veltrano Funeral Home we offer a broad range of burial options in Maple Ridge, NY, and we invite you to read about all that's possible. We're here to help you design a service and a physical memorial that will be a beautiful place to visit, forevermore.</p>

  <h2 class="band band--section band--graveside">GRAVESIDE FUNERAL SERVICES</h2>
  <p class="abs kicker kicker--graveside">Express the life of your loved one and create a place for family and friends to gather.</p>
  <p class="abs body body--graveside">We can help you design a meaningful and healing service to take place at the graveside. These services can take place outdoors or even inside a mausoleum. We'll guide you through the process of personalizing both the service and the site in multiple ways. Working with your Funeral Director, you can select readings, speakers and create spiritual moments. You can include military honors, masonic rites and religious leadership. When it comes to memorialization, we offer many options. Your selection may include a flat memorial, upright monument, ledger, mausoleum plate, memorial benches or private estates. We're here to share our expertise, with professionalism and compassion. Contact us with any questions you may have.</p>

  <h2 class="band band--section band--committal">COMMITTAL SERVICES</h2>
  <p class="abs kicker kicker--committal">A graveside service takes place after a funeral and can be a profound healing experience.</p>
  <p class="abs body body--committal">Funerals often take place at the mortuary chapel or at your place of religious worship. In that case, an internment and committal service can follow at the graveside. These are important gatherings to commemorate a life and mark the end of physical closeness. Family and friends gather to commit a loved one to the earth and say final farewells together. A committal service is symbolic and a helpful step in healing.</p>

  <h2 class="band band--section band--immediate">IMMEDIATE BURIALS</h2>
  <p class="abs kicker kicker--immediate">Together with your funeral professional, we can guide you through all of the arrangements</p>
  <p class="abs body body--immediate">Burials are often an unexpected need, and we can handle every detail should this option make sense for you and your family. Please call us any time to discuss your needs. Our mission is to ease your burden.</p>

  <div class="photo photo--roses" role="img" aria-label="Yellow and red roses resting on a polished casket"></div>
  <div class="abs brand brand--right"><span class="brand__dot"></span><span>Arthur J. Veltrano<br>Funeral Home</span></div>
</section>

</body>
</html>
```